Net Clarity Partners Needs a New Business Card Design

Attached is my new logo that ArtFlockly created and picture of me for the back of the business card. Also attached is the information to include on the business card (on my existing business card design - NCP1 file attached).

The designer also provided a treatment of my logo that I really like if you can use it somehow. Also attached - file name "Preferred Version of New Logo."

Marla Quinteros

Net Clarity Partners
4817 Brindle Ave., #315
Houston, TX 77056

Tel: (832) 555-0147
www.netclaritypartners.example
marla@netclaritypartners.example

Thank you.

Target Market(s)

attorneys and law firms

Industry/Entity Type

Legal

Contact Information for Business Card

Proved in the Project Description

Font styles to use
Other font styles liked:
• I am open on font - no script though.

Colors
2d73b3
33a6d7

Requirements
Must have
• my logo
• company name & contact info
• my picture on the back
• colors that coordinate with the logo
Nice to have
• love to use the treated version of the logo if possible

```html
<!DOCTYPE html>
<html lang="en">
<head>
<meta charset="utf-8">
<title>Net Clarity Partners – Business Card</title>
<link href="https://fonts.googleapis.com/css2?family=Arimo:wght@400;700&display=swap" rel="stylesheet">
<style>
  :root {
    --backdrop: #2b2c2e;
    --card-top: #34414b;
    --card-bottom: #1b242b;
    --accent: #33a6d7;
    --brand-blue: #2d73b3;
    --text-light: #e6edf2;
    --photo-top: #6a6f8c;
    --photo-bottom: #2b3590;
  }
  * { margin: 0; padding: 0; box-sizing: border-box; }
  html, body {
    width: 1200px; height: 997px; overflow: hidden;
    background: var(--backdrop);
    font-family: "Arimo", Arial, sans-serif;
  }
  .canvas { position: relative; width: 1200px; height: 997px; }

  .card {
    position: absolute;
    width: 600px; height: 343px;
    border-radius: 18px;
    overflow: hidden;
    background: linear-gradient(160deg, var(--card-top), var(--card-bottom));
    box-shadow: 0 14px 30px rgba(0,0,0,.55);
  }
  .card--front { left: 90px; top: 90px; }
  .card--back  { left: 510px; top: 520px; }

  .brand-square { flex: none; width: 22px; height: 22px; background: var(--accent); }
  .brand-name {
    font-weight: 700; font-size: 24px; color: var(--accent);
    text-transform: uppercase; letter-spacing: 1px; white-space: nowrap;
  }

  /* Front side */
  .front-logo {
    position: absolute; left: 190px; top: 64px;
    display: flex; align-items: center; gap: 10px;
  }

  .accent-band {
    position: absolute; left: 0; right: 0; top: 126px; height: 34px;
    background: var(--accent);
  }
  .person {
    position: absolute; right: 24px; top: 128px; text-align: right;
    color: var(--text-light);
  }
  .person-name { font-size: 16px; line-height: 18px; }
  .person-title { font-size: 10px; line-height: 12px; font-weight: 700; }

  .contact-list {
    position: absolute; right: 22px; top: 178px;
    list-style: none; text-align: right; color: var(--text-light);
    font-size: 13px;
  }
  .contact-list li {
    display: flex; justify-content: flex-end; align-items: center;
    gap: 10px; height: 26px; white-space: nowrap;
  }
  .contact-list svg { flex: none; width: 12px; height: 12px; fill: var(--accent); }

  .portrait {
    position: absolute; left: 0; bottom: 0; width: 250px; height: 183px;
    background: linear-gradient(180deg, var(--photo-top), var(--photo-bottom));
  }

  /* Back side */
  .back-logo {
    position: absolute; left: 0; right: 0; top: 150px;
    display: flex; justify-content: center; align-items: center; gap: 12px;
  }
  .back-logo .brand-square { width: 28px; height: 28px; }
  .back-logo .brand-name { font-size: 32px; }
</style>
</head>
<body>
<main class="canvas">

  <section class="card card--front" aria-label="Business card, contact side">
    <div class="front-logo">
      <span class="brand-square"></span>
      <span class="brand-name">Net Clarity Partners</span>
    </div>

    <div class="accent-band"></div>
    <div class="person">
      <p class="person-name">Marla Quinteros</p>
      <p class="person-title">Owner</p>
    </div>

    <ul class="contact-list">
      <li>(832) 555-0147
        <svg viewBox="0 0 24 24" aria-hidden="true"><path d="M6.6 10.8a15 15 0 0 0 6.6 6.6l2.2-2.2a1 1 0 0 1 1-.25 11.4 11.4 0 0 0 3.6.57 1 1 0 0 1 1 1V20a1 1 0 0 1-1 1A17 17 0 0 1 3 4a1 1 0 0 1 1-1h3.5a1 1 0 0 1 1 1c0 1.25.2 2.45.57 3.6a1 1 0 0 1-.25 1z"/></svg>
      </li>
      <li>marla@netclaritypartners.example
        <svg viewBox="0 0 24 24" aria-hidden="true"><path d="M2 5h20v14H2z M4 7v.5l8 5 8-5V7l-8 5z" fill-rule="evenodd"/></svg>
      </li>
      <li>4817 Brindle Ave., #315, Houston, TX 77056
        <svg viewBox="0 0 24 24" aria-hidden="true"><path d="M12 2a7 7 0 0 0-7 7c0 5.25 7 13 7 13s7-7.75 7-13a7 7 0 0 0-7-7zm0 9.5A2.5 2.5 0 1 1 12 6.5a2.5 2.5 0 0 1 0 5z"/></svg>
      </li>
    </ul>

    <div class="portrait" role="img" aria-label="Portrait photo of Marla Quinteros"></div>
  </section>

  <section class="card card--back" aria-label="Business card, logo side">
    <div class="back-logo">
      <span class="brand-square"></span>
      <span class="brand-name">Net Clarity Partners</span>
    </div>
  </section>

</main>
</body>
</html>
```